Offshore Energy Projects Management Consultancy needs a business card design

Logo available. We provide teams to deliver engineering consultancy, project management and delivery teams mainly in the offshore renewables sector. The company is all about bringing the right people to a project to deliver the scope.

The business card will be used for all staff.

The business card should be quite simple, vibrant and uncluttered but convey experience, enthusiasm and integration.

Target Market(s)

Energy Project Developers and Tier 1 construction companies

Contact Information for Business Card

Logo should be on the back of the card. I'm happy for the designer to play with the colour of the logo and background colour.

Front of the card should convey all the must have information in a clear and professional manner but without being overly traditional.

Colors

Designer to choose colors to be used in the design.

Requirements
Must have
• Land Line Tel Number, Mobile Tel Number, Email, business address, web address.

```html
<!DOCTYPE html>
<html lang="en">
<head>
<meta charset="utf-8">
<title>Tidewater Project Partners – Business Card</title>
<link rel="stylesheet" href="https://fonts.googleapis.com/css2?family=Open+Sans:wght@400;600&family=Arimo:wght@400&family=Montserrat:wght@600&display=swap">
<style>
  :root {
    --canvas: #e6e9eb;
    --card-dark: #1d1f20;
    --card-light: #ebeae6;
    --brand-blue: #1f7fd0;
    --edge-blue: #1565c0;
    --ink: #1a1a1a;
    --muted: #3a3a3a;
  }
  * { box-sizing: border-box; margin: 0; padding: 0; }
  html, body { width: 1200px; height: 900px; overflow: hidden; }
  body {
    background: var(--canvas);
    display: flex;
    flex-direction: column;
    align-items: center;
    justify-content: center;
    gap: 56px;
    font-family: "Arimo", Arial, sans-serif;
  }
  .card {
    position: relative;
    width: 640px;
    height: 366px;
    border-right: 3px solid var(--edge-blue);
    border-bottom: 3px solid var(--edge-blue);
    box-shadow: 0 6px 18px rgba(0,0,0,0.12);
  }

  /* Back of card */
  .card-back {
    background: var(--card-dark);
    display: flex;
    align-items: center;
    justify-content: center;
  }
  .brand-lockup {
    display: flex;
    align-items: center;
    gap: 18px;
  }
  .brand-dot {
    width: 34px;
    height: 34px;
    border-radius: 50%;
    background: var(--brand-blue);
  }
  .brand-name {
    font-family: "Montserrat", sans-serif;
    font-weight: 600;
    color: var(--brand-blue);
    text-transform: uppercase;
    letter-spacing: 0.04em;
    font-size: 30px;
    line-height: 1.1;
  }

  /* Front of card */
  .card-front { background: var(--card-light); }
  .holder {
    position: absolute;
    top: 40px;
    right: 44px;
    text-align: right;
    font-family: "Open Sans", sans-serif;
  }
  .holder-name {
    color: var(--brand-blue);
    font-size: 30px;
    font-weight: 400;
    line-height: 1.1;
  }
  .holder-role {
    color: var(--ink);
    font-size: 13px;
    margin-top: 2px;
  }
  .front-brand {
    position: absolute;
    left: 40px;
    top: 200px;
    display: flex;
    align-items: center;
    gap: 10px;
  }
  .front-brand .brand-dot { width: 20px; height: 20px; }
  .front-brand .brand-name { font-size: 15px; }
  .divider {
    position: absolute;
    left: 262px;
    top: 120px;
    width: 2px;
    height: 210px;
    background: var(--ink);
  }
  .contact-list {
    position: absolute;
    left: 280px;
    top: 140px;
    list-style: none;
  }
  .contact-item {
    display: flex;
    align-items: center;
    gap: 14px;
    height: 33px;
    font-size: 14px;
    color: var(--ink);
    text-transform: uppercase;
  }
  .contact-icon { width: 16px; height: 16px; flex: none; }
</style>
</head>
<body>

<section class="card card-back" aria-label="Back of business card">
  <div class="brand-lockup">
    <span class="brand-dot"></span>
    <span class="brand-name">Tidewater<br>Project Partners</span>
  </div>
</section>

<section class="card card-front" aria-label="Front of business card">
  <div class="holder">
    <p class="holder-name">Elena Marsh</p>
    <p class="holder-role">Founder</p>
  </div>

  <div class="front-brand">
    <span class="brand-dot"></span>
    <span class="brand-name">Tidewater<br>Project Partners</span>
  </div>

  <span class="divider"></span>

  <ul class="contact-list">
    <li class="contact-item">
      <svg class="contact-icon" viewBox="0 0 16 16" aria-hidden="true"><path d="M3 1.5l3 3-1.5 2c1 2 2.5 3.5 4.5 4.5l2-1.5 3 3-2 2C6 14 2 10 1.5 3.5z" fill="#1a1a1a"/></svg>
      0198 765 4321
    </li>
    <li class="contact-item">
      <svg class="contact-icon" viewBox="0 0 16 16" aria-hidden="true"><rect x="4" y="1" width="8" height="14" rx="1.5" fill="none" stroke="#1a1a1a" stroke-width="1.5"/><circle cx="8" cy="12.5" r="0.9" fill="#1a1a1a"/></svg>
      0176 543 2109
    </li>
    <li class="contact-item">
      <svg class="contact-icon" viewBox="0 0 16 16" aria-hidden="true"><rect x="1" y="3" width="14" height="10" fill="#1a1a1a"/><path d="M1 3l7 5.5L15 3" fill="none" stroke="#ebeae6" stroke-width="1.2"/></svg>
      hello@tidewaterpartners.co.in
    </li>
    <li class="contact-item">
      <svg class="contact-icon" viewBox="0 0 16 16" aria-hidden="true"><path d="M8 15s5-5.5 5-9A5 5 0 0 0 3 6c0 3.5 5 9 5 9z" fill="#1a1a1a"/><circle cx="8" cy="6" r="1.8" fill="#ebeae6"/></svg>
      45, Harbour Road
    </li>
    <li class="contact-item">
      <svg class="contact-icon" viewBox="0 0 16 16" aria-hidden="true"><g fill="none" stroke="#1a1a1a" stroke-width="1.2"><circle cx="8" cy="8" r="6.5"/><ellipse cx="8" cy="8" rx="3" ry="6.5"/><path d="M1.5 8h13M2.5 4.5h11M2.5 11.5h11"/></g></svg>
      www.tidewaterpartners.co.in
    </li>
  </ul>
</section>

</body>
</html>
```